Portrait of a Graduate

Our school community has created a document which describes the characteristics that every student who graduates from our school should possess. We would like a visual graphic to present the information to parents\ community. We came up with three buckets (Personal, Social, and Academic) and the concept "BLH Graduates Will Be Okay" is the central theme.
We are open to 2 different concepts:
1. A ven diagram of sorts, where the three buckets are each in an area - and the over lap is "BLH Graduates Will Be Okay"
2. Our logo has a sassafras leaf in it - using the leaves to represent each bucket and the central concept as the stem - or some other creative version.

The text to be used is below:

BLH Graduates Will Be Okay (at the center/on the stem)

1. Personal
They will:
have self-worth
advocate for themselves
feel secure in their future

2. Social
They will:
embrace differences
engage in trusting relationships
be compassionate (members of their community)

3. Academic
They will:
apply skills and strategies
creatively problem-solve
achieve individual success

```html
<!DOCTYPE html>
<html lang="en">
<head>
<meta charset="utf-8">
<title>Portrait of a Graduate – BLH</title>
<link rel="stylesheet" href="https://fonts.googleapis.com/css2?family=Marcellus&family=Lora:wght@400;700&display=swap">
<style>
  :root {
    --paper: #ffffff;
    --gold: #cfb843;
    --navy: #2a394b;
    --forest: #344f33;
    --ink: #1f2b3d;
    --text-on-dark: #ffffff;
  }
  html, body {
    margin: 0;
    padding: 0;
    width: 1200px;
    height: 1186px;
    overflow: hidden;
    background: var(--paper);
  }
  .portrait {
    display: block;
    width: 1200px;
    height: 1186px;
  }
  .school-name {
    font-family: "Lora", serif;
    font-weight: 400;
    fill: var(--ink);
  }
  .theme-title {
    font-family: "Marcellus", serif;
    font-size: 60px;
    fill: var(--gold);
    letter-spacing: 1px;
  }
  .trait {
    font-family: "Lora", serif;
    font-size: 20px;
    fill: var(--text-on-dark);
  }
  .trait-note {
    font-family: "Lora", serif;
    font-size: 12.5px;
    fill: var(--text-on-dark);
  }
  .bucket-title {
    font-family: "Lora", serif;
    font-weight: 700;
    font-size: 22px;
    fill: var(--ink);
  }
  .bucket-lead {
    font-family: "Lora", serif;
    font-size: 16px;
    fill: var(--ink);
  }
</style>
</head>
<body>
<svg class="portrait" viewBox="0 0 1500 1482.5" xmlns="http://www.w3.org/2000/svg">
  <defs>
    <clipPath id="clip-personal"><circle cx="745" cy="648" r="178"/></clipPath>
    <clipPath id="clip-academic"><circle cx="540" cy="1003" r="178"/></clipPath>
    <clipPath id="clip-social"><circle cx="950" cy="1003" r="178"/></clipPath>
    <linearGradient id="lens-personal" x1="0" y1="0" x2="1" y2="0">
      <stop offset="0" stop-color="#ffffff"/>
      <stop offset="1" stop-color="#e3dbc3"/>
    </linearGradient>
    <linearGradient id="lens-academic" x1="0" y1="0" x2="1" y2="1">
      <stop offset="0" stop-color="#ffffff"/>
      <stop offset="1" stop-color="#c3c9df"/>
    </linearGradient>
    <linearGradient id="lens-social" x1="0" y1="0" x2="1" y2="0">
      <stop offset="0" stop-color="#ffffff"/>
      <stop offset="1" stop-color="#74907a"/>
    </linearGradient>
  </defs>

  <!-- School name -->
  <g class="school-lockup">
    <circle cx="762" cy="250" r="10" fill="var(--ink)"/>
    <text class="school-name" x="765" y="300" text-anchor="middle" font-size="30">THE BRAMBLE LANE SCHOOL</text>
    <text class="school-name" x="765" y="345" text-anchor="middle" font-size="30">at HARTWELL</text>
  </g>

  <text class="theme-title" x="771" y="445" text-anchor="middle">BLH GRADUATES WILL BE OKAY</text>

  <!-- Personal -->
  <g class="bucket bucket-personal">
    <circle cx="745" cy="648" r="178" fill="var(--gold)"/>
    <g clip-path="url(#clip-personal)">
      <circle cx="745" cy="905" r="200" fill="url(#lens-personal)" stroke="#f4e98a" stroke-width="3"/>
    </g>
    <polygon points="730,822 760,822 745,845" fill="#ebe6d8"/>
    <text class="trait" text-anchor="middle">
      <tspan x="748" y="550">HAVE SELF-WORTH</tspan>
      <tspan x="748" y="594">ADVOCATE FOR</tspan>
      <tspan x="748" y="612">THEMSELVES</tspan>
      <tspan x="748" y="657">FEEL SECURE IN THEIR</tspan>
      <tspan x="748" y="676">FUTURE</tspan>
    </text>
    <text class="bucket-title" x="749" y="762" text-anchor="middle">I. PERSONAL</text>
    <text class="bucket-lead" x="749" y="782" text-anchor="middle">They will:</text>
  </g>

  <!-- Academic -->
  <g class="bucket bucket-academic">
    <circle cx="540" cy="1003" r="178" fill="var(--navy)"/>
    <g clip-path="url(#clip-academic)">
      <circle cx="792" cy="852" r="220" fill="url(#lens-academic)" stroke="#5d7396" stroke-width="3"/>
    </g>
    <polygon points="684,905 712,905 700,930" fill="#d4d8e8"/>
    <text class="trait" text-anchor="middle">
      <tspan x="477" y="913">APPLY SKILLS</tspan>
      <tspan x="477" y="934">AND STRATEGIES</tspan>
      <tspan x="492" y="1021">CREATIVELY</tspan>
      <tspan x="492" y="1042">PROBLEM-SOLVE</tspan>
      <tspan x="535" y="1130">ACHIEVE INDIVIDUAL</tspan>
      <tspan x="535" y="1151">SUCCESS</tspan>
    </text>
    <g transform="translate(650,948) rotate(60)">
      <text class="bucket-title" x="0" y="0" text-anchor="middle">III. ACADEMIC</text>
      <text class="bucket-lead" x="-28" y="20" text-anchor="middle">They will:</text>
    </g>
  </g>

  <!-- Social -->
  <g class="bucket bucket-social">
    <circle cx="950" cy="1003" r="178" fill="var(--forest)"/>
    <g clip-path="url(#clip-social)">
      <circle cx="698" cy="852" r="220" fill="url(#lens-social)" stroke="#5d9a56" stroke-width="3"/>
    </g>
    <polygon points="778,905 806,905 790,930" fill="#eef1ee"/>
    <text class="trait" text-anchor="middle">
      <tspan x="1000" y="906">EMBRACE</tspan>
      <tspan x="1000" y="926">DIFFERENCES</tspan>
      <tspan x="1000" y="1009">ENGAGE IN</tspan>
      <tspan x="1000" y="1029">TRUSTING</tspan>
      <tspan x="1000" y="1050">RELATIONSHIPS</tspan>
      <tspan x="946" y="1103">BE COMPASSIONATE</tspan>
    </text>
    <text class="trait-note" x="946" y="1123" text-anchor="middle">(MEMBERS OF THEIR COMMUNITY)</text>
    <g transform="translate(848,942) rotate(-60)">
      <text class="bucket-title" x="0" y="0" text-anchor="middle">II. SOCIAL</text>
      <text class="bucket-lead" x="12" y="20" text-anchor="middle">They will:</text>
    </g>
  </g>
</svg>
</body>
</html>
```